Committee to Elect Big Ned Harlow County Commissioner District 1

I need a patriotic Background with Bold Red White and Blue Colors with a steel'ish look. The Front will say "Vote Big Ned Harlow County Commissioner" With an Emphasis on the name "Harlow" The back needs to be simple color that allows for readable lines. It will have my website, phone, email and facebook links on the back and in small but readable print on the bottom it will say "Paid for by the Committe to Elect Big Ned Harlow County Commissiner"

```html
<!DOCTYPE html>
<html lang="en">
<head>
<meta charset="utf-8">
<title>Big Ned Harlow for County Commissioner – Cards</title>
<link href="https://fonts.googleapis.com/css2?family=Montserrat:wght@900&family=Oswald:wght@500&family=Questrial&display=swap" rel="stylesheet">
<style>
  :root {
    --page-bg: #3a3a3c;
    --navy: #102552;
    --red: #d81f26;
    --blue-deep: #082a78;
    --blue-mid: #1040a8;
    --blue-light: #2a5cc4;
    --white: #ffffff;
    --ray-grey: #ececee;
    --ink: #1d1d1f;
  }
  * { box-sizing: border-box; margin: 0; padding: 0; }
  html, body { width: 1200px; height: 1200px; overflow: hidden; }
  body { background: var(--page-bg); position: relative; }

  .card {
    position: absolute;
    left: 150px;
    width: 900px;
    height: 514px;
    border-radius: 34px;
    overflow: hidden;
    background:
      repeating-conic-gradient(from 0deg at 50% 55%, rgba(0,0,0,.035) 0deg 6deg, transparent 6deg 14deg),
      radial-gradient(ellipse at 50% 50%, var(--white) 35%, var(--ray-grey) 100%);
    box-shadow: 0 10px 24px rgba(0,0,0,.35);
  }
  .card--back { top: 56px; }
  .card--front { top: 630px; }

  .band {
    position: absolute;
    left: 0; right: 0;
    background:
      repeating-linear-gradient(90deg, rgba(255,255,255,.04) 0 2px, rgba(0,0,0,.04) 2px 4px),
      linear-gradient(90deg, var(--blue-mid), var(--blue-deep) 30%, var(--blue-light) 55%, var(--blue-deep) 80%, var(--blue-mid));
  }
  .band--top { top: 0; height: 72px; border-bottom: 9px solid var(--red); }
  .band--bottom { bottom: 0; height: 112px; border-top: 9px solid var(--red); }
  .card--back .band--top { height: 60px; }
  .card--back .band--bottom { height: 120px; }

  /* back */
  .contact-list {
    position: absolute;
    left: 300px;
    top: 150px;
    list-style: none;
    font-family: "Questrial", sans-serif;
    font-size: 32px;
    color: var(--ink);
  }
  .contact-list li {
    display: flex;
    align-items: center;
    gap: 14px;
    height: 54px;
    white-space: nowrap;
  }
  .contact-icon {
    width: 38px; height: 38px;
    flex: none;
    border-radius: 50%;
    background: var(--red);
    display: flex; align-items: center; justify-content: center;
  }
  .disclaimer {
    position: absolute;
    left: 0; right: 0; bottom: 38px;
    text-align: center;
    font-family: "Oswald", sans-serif;
    font-weight: 500;
    font-size: 22px;
    letter-spacing: 1.5px;
    color: var(--white);
    text-transform: uppercase;
  }

  /* front */
  .headline {
    position: absolute;
    left: 0; right: 0; top: 112px;
    text-align: center;
    font-family: "Montserrat", sans-serif;
    font-weight: 900;
    color: var(--navy);
    text-transform: uppercase;
    line-height: 1;
  }
  .headline__lead { font-size: 64px; letter-spacing: 1px; }
  .headline__name { font-size: 112px; letter-spacing: 1px; margin-top: 8px; }
  .headline__office { margin-top: 14px; font-size: 42px; letter-spacing: 5px; }
</style>
</head>
<body>

  <section class="card card--back" aria-label="Card back">
    <div class="band band--top"></div>
    <ul class="contact-list">
      <li>
        <span class="contact-icon">
          <svg width="22" height="22" viewBox="0 0 24 24"><path fill="#fff" d="M6.6 10.8c1.4 2.8 3.8 5.1 6.6 6.6l2.2-2.2c.3-.3.7-.4 1-.2 1.1.4 2.3.6 3.6.6.6 0 1 .4 1 1V20c0 .6-.4 1-1 1C10.6 21 3 13.4 3 4c0-.6.4-1 1-1h3.5c.6 0 1 .4 1 1 0 1.3.2 2.5.6 3.6.1.3 0 .7-.2 1z"/></svg>
        </span>
        (555) 014-2290
      </li>
      <li>
        <span class="contact-icon">
          <svg width="22" height="22" viewBox="0 0 24 24"><rect x="3" y="6" width="18" height="12" fill="none" stroke="#fff" stroke-width="2"/><path d="M3 6l9 7 9-7" fill="none" stroke="#fff" stroke-width="2"/></svg>
        </span>
        info@harlowforcounty.org
      </li>
      <li>
        <span class="contact-icon">
          <svg width="24" height="24" viewBox="0 0 24 24" fill="none" stroke="#fff" stroke-width="1.6"><circle cx="12" cy="12" r="8"/><ellipse cx="12" cy="12" rx="3.5" ry="8"/><path d="M4 12h16M5.5 8h13M5.5 16h13"/></svg>
        </span>
        www.harlowforcounty.org
      </li>
      <li>
        <span class="contact-icon"></span>
        @harlowforcounty
      </li>
    </ul>
    <div class="band band--bottom">
      <p class="disclaimer">Paid for by the Committe to Elect Big Ned Harlow County Commissiner</p>
    </div>
  </section>

  <section class="card card--front" aria-label="Card front">
    <div class="band band--top"></div>
    <div class="headline">
      <div class="headline__lead">Vote Big Ned</div>
      <div class="headline__name">Harlow</div>
      <div class="headline__office">County Commissioner</div>
    </div>
    <div class="band band--bottom"></div>
  </section>

</body>
</html>
```